Software Company Business Card

We are looking for a new design of our business card. The design will also be used in the rest of our branding and marketing materials as we want to keep it all uniform. We sell POS software to fine/luxury jewelers and also offer other business services as well to help the jeweler manage their business and need something more updated, technical and fresh, preferably more on the masculine side. We do not want any designs with gems in them but if possible would like to incorporate the circle and arrow in the logo into the design, but not a requirement if you can't make it work. I would like to see a variety of the mix. The colors need to remain our blue and orange and the logo can not change. The squiggly lines have been used as our corporate identity for over 20 years and its time to update. Our company name is TELK (Superior Counter Operations Platforms).

Target Market(s)

High End Jewelers

Industry/Entity Type

Software

Contact Information for Business Card

As seen in attached image

Requirements
Must have
• Our logo and the colors must remain the same. Blue is #d95d39 and Orange is #0f5682.
Nice to have
• The circle and arrow incorporated but not a requirement.
Should not have
• Anything jewelry or gem related.

```html
<!DOCTYPE html>
<html lang="en">
<head>
<meta charset="utf-8">
<title>TELK Business Card</title>
<link rel="stylesheet" href="https://fonts.googleapis.com/css2?family=Open+Sans:wght@400;600;800&display=swap">
<style>
  :root {
    --brand-blue: #14557f;
    --brand-orange: #d35a37;
    --card-white: #f4f4f4;
    --ink: #2b2b2b;
    --backdrop: #e6e7e7;
    --badge-gold: #c19a4a;
    --badge-sage: #8ea89a;
  }
  * { margin: 0; padding: 0; box-sizing: border-box; }
  html, body { width: 1200px; height: 960px; overflow: hidden; }
  body {
    background: var(--backdrop);
    font-family: "Open Sans", Arial, sans-serif;
    position: relative;
  }
  .card {
    position: absolute;
    left: 304px;
    width: 594px;
    height: 340px;
    overflow: hidden;
  }
  /* Front */
  .card-front { top: 117px; background: var(--brand-blue); }
  .front-circle {
    position: absolute; left: 36px; top: 35px;
    width: 270px; height: 270px; border-radius: 50%;
    background: var(--brand-orange);
  }
  .front-wordmark {
    position: absolute; left: 338px; top: 128px;
    color: #fff; font-weight: 800; font-size: 66px;
    line-height: 1; letter-spacing: -1px;
  }
  .front-tagline {
    position: absolute; left: 342px; top: 190px;
    color: #fff; font-weight: 800; font-size: 10px;
    text-transform: uppercase; letter-spacing: 0.1px;
  }
  /* Back */
  .card-back { top: 511px; background: var(--card-white); }
  .back-wordmark {
    position: absolute; left: 36px; top: 22px;
    color: var(--brand-blue); font-weight: 800; font-size: 64px;
    line-height: 1; letter-spacing: -1px;
  }
  .back-tagline {
    position: absolute; left: 40px; top: 89px;
    color: var(--brand-orange); font-weight: 800; font-size: 10.5px;
    text-transform: uppercase;
  }
  .back-circle {
    position: absolute; left: 283px; top: 37px;
    width: 64px; height: 64px; border-radius: 50%;
    background: var(--brand-orange);
  }
  .badge { position: absolute; left: 37px; width: 182px; }
  .badge-show { top: 175px; height: 62px; background: var(--badge-gold); border-radius: 31px 6px 6px 31px; }
  .badge-society { top: 246px; height: 42px; background: var(--badge-sage); border-radius: 4px; }
  .rule { position: absolute; left: 284px; width: 2px; }
  .rule-name { top: 135px; height: 40px; background: var(--brand-blue); }
  .rule-contact { top: 181px; height: 114px; background: var(--brand-orange); }
  .person { position: absolute; left: 304px; top: 131px; }
  .person-name { color: var(--brand-blue); font-size: 20px; font-weight: 600; line-height: 26px; }
  .person-title { color: var(--ink); font-size: 16px; line-height: 20px; }
  .contact { position: absolute; left: 304px; top: 192px; color: var(--ink); font-size: 16px; line-height: 20px; }
  .address { margin-bottom: 7px; }
  .contact-line { display: flex; align-items: center; gap: 5px; }
  .contact-line svg { width: 12px; height: 12px; fill: var(--brand-orange); flex: none; }
  .footer-bands { position: absolute; left: 0; top: 307px; }
  .website {
    position: absolute; left: 37px; top: 310px;
    color: #fff; font-size: 15px; letter-spacing: 1.2px; line-height: 22px;
  }
</style>
</head>
<body>
  <section class="card card-front">
    <div class="front-circle"></div>
    <div class="front-wordmark">telk</div>
    <div class="front-tagline">Business &amp; Technology Solutions</div>
  </section>

  <section class="card card-back">
    <div class="back-wordmark">telk</div>
    <div class="back-tagline">Business &amp; Technology Solutions</div>
    <div class="back-circle"></div>

    <div class="badge badge-show"></div>
    <div class="badge badge-society"></div>

    <div class="rule rule-name"></div>
    <div class="rule rule-contact"></div>

    <div class="person">
      <div class="person-name">Dorian Pellham</div>
      <div class="person-title">Director of Global Operations</div>
    </div>

    <div class="contact">
      <div class="address">4815 Meridian Parkway, Suite 210<br>Carson Falls, NV 89110</div>
      <div class="contact-line">
        <svg viewBox="0 0 24 24"><path d="M6.6 10.8a15.1 15.1 0 0 0 6.6 6.6l2.2-2.2a1 1 0 0 1 1-.25 11.4 11.4 0 0 0 3.6.57 1 1 0 0 1 1 1V20a1 1 0 0 1-1 1A17 17 0 0 1 3 4a1 1 0 0 1 1-1h3.5a1 1 0 0 1 1 1c0 1.25.2 2.45.57 3.57a1 1 0 0 1-.25 1z"/></svg>
        <span>+1 800 555-0142</span>
      </div>
      <div class="contact-line">
        <svg viewBox="0 0 24 24"><path d="M6 2h10v5H6zM3 8h18a1 1 0 0 1 1 1v8h-4v5H6v-5H2V9a1 1 0 0 1 1-1zm5 8v4h8v-4z"/></svg>
        <span>+1 702 555-0187</span>
      </div>
      <div class="contact-line">
        <svg viewBox="0 0 24 24"><path d="M2 5h20v14H2zm2 2v.5l8 5 8-5V7zm0 2.9V17h16V9.9l-8 5z"/></svg>
        <span>dorian@telkpos.com</span>
      </div>
    </div>

    <svg class="footer-bands" width="594" height="33" viewBox="0 0 594 33">
      <polygon points="0,0 236,0 263,33 0,33" fill="var(--brand-orange)"/>
      <polygon points="252,16 594,16 594,33 266,33" fill="var(--brand-blue)"/>
    </svg>
    <div class="website">www.telkpos.com</div>
  </section>
</body>
</html>
```